TR & Groundworks
Landscaping
TR & Groundworks - Utilities
Creative Brief
Professional
Dennis Holloway
Brisk Meadow Cooling and Yardcraft LLP
P.O. Box 618207 Christiansted, St. Croix 00822
Briskmeadowcoolingandyardcraft@mailvessel.com
Mona Fairweather is the Co-Owner name needs to be on card also

```html
<!DOCTYPE html>
<html lang="en">
<head>
<meta charset="utf-8">
<title>Brisk Meadow – Stationery Set</title>
<link href="https://fonts.googleapis.com/css2?family=Roboto:ital,wght@0,400;0,700;0,900&display=swap" rel="stylesheet">
<style>
  :root{
    --blue-deep:#1553a8;
    --blue:#2a78d0;
    --blue-light:#6db6ee;
    --green:#6fb52c;
    --green-light:#c5e06a;
    --gray:#a3a6aa;
    --gray-light:#e4e5e7;
    --ink:#3a3a3a;
    --paper:#ffffff;
  }
  *{margin:0;padding:0;box-sizing:border-box}
  html,body{width:1200px;height:741px;overflow:hidden;background:var(--paper)}
  body{position:relative;font-family:"Roboto",Arial,sans-serif;color:var(--ink)}
  .sheet{position:absolute;overflow:hidden;background:var(--paper);box-shadow:0 0 3px rgba(0,0,0,.35)}
  .sheet svg.deco{position:absolute;inset:0;width:100%;height:100%}
  .brand{position:absolute;display:flex;align-items:center;gap:6px}
  .brand-dot{border-radius:50%;background:var(--blue);flex:none}
  .brand-name{font-weight:900;color:var(--blue-deep);white-space:nowrap;line-height:1}
  .mark{position:absolute;display:flex;flex-direction:column;align-items:center;gap:8px;left:50%;top:50%;transform:translate(-50%,-50%)}
  .mark-circle{width:74px;height:74px;border-radius:50%;background:radial-gradient(circle at 40% 35%,#ffffff 0,#dfeefb 45%,var(--blue) 100%);border:3px solid #fff}
  .mark-name{font-weight:900;font-size:13px;color:#fff;white-space:nowrap}

  /* business card front */
  .card-front{left:168px;top:84px;width:216px;height:127px}
  .card-front .brand{left:10px;top:14px}
  .card-front .brand-dot{width:22px;height:22px}
  .card-front .brand-name{font-size:13px}
  .holder{position:absolute;left:74px;top:44px;text-align:center}
  .holder-name{font-size:8px;font-weight:700;color:var(--ink)}
  .holder-role{font-size:4.5px;color:#777;margin-top:1px}
  .card-contact{position:absolute;left:10px;top:68px;font-size:4.6px;line-height:1.45;color:var(--ink)}
  .card-contact b{font-weight:700}

  .card-green{left:396px;top:84px;width:223px;height:127px;background:linear-gradient(100deg,var(--green) 0%,#9bcc3d 50%,var(--green-light) 100%)}
  .card-blue{left:168px;top:228px;width:216px;height:127px;background:radial-gradient(ellipse at 50% 50%,var(--blue-light) 0%,var(--blue) 55%,var(--blue-deep) 100%)}
  .card-gray{left:396px;top:228px;width:223px;height:127px;background:radial-gradient(ellipse at 50% 50%,#fbfbfb 0%,var(--gray-light) 50%,var(--gray) 100%)}
  .card-gray .mark-name{color:var(--blue-deep)}

  /* envelope */
  .envelope{left:38px;top:372px;width:581px;height:295px}
  .envelope .brand{left:30px;top:90px}
  .envelope .brand-dot{width:36px;height:36px}
  .envelope .brand-name{font-size:22px}
  .envelope .flap-circle{position:absolute;left:50%;top:6px;width:44px;height:44px;margin-left:-22px;border-radius:50%;background:radial-gradient(circle at 40% 35%,#fff 0,#dfeefb 45%,var(--blue) 100%);border:2px solid #fff}
  .env-address{position:absolute;left:30px;top:148px;font-size:10px;line-height:1.35;color:var(--ink)}

  /* letterhead */
  .letterhead{left:634px;top:19px;width:523px;height:701px}
  .letterhead .brand{left:22px;top:16px}
  .letterhead .brand-dot{width:32px;height:32px}
  .letterhead .brand-name{font-size:19px}
  .lh-footer{position:absolute;left:22px;top:645px;font-size:8px;line-height:1.45;color:var(--ink)}
  .lh-footer b{font-weight:700}
</style>
</head>
<body>

<section class="sheet card-front" aria-label="Business card front">
  <svg class="deco" viewBox="0 0 216 127" preserveAspectRatio="none">
    <path d="M170 0 Q150 63 170 127 L216 127 L216 0 Z" fill="var(--gray)"/>
    <path d="M178 0 Q160 63 178 127 L216 127 L216 0 Z" fill="var(--blue)"/>
    <path d="M190 0 Q176 63 190 127 L216 127 L216 0 Z" fill="var(--blue-deep)"/>
  </svg>
  <div class="brand"><span class="brand-dot"></span><span class="brand-name">Brisk Meadow</span></div>
  <div class="holder">
    <div class="holder-name">Dennis Holloway</div>
    <div class="holder-role">Managing Partner</div>
    <div class="holder-role">Mona Fairweather, Co-Owner</div>
  </div>
  <div class="card-contact">
    P.O. Box 618207<br>
    Christiansted, St. Croix 00822<br>
    <b>Ph:</b> 340-555-0182<br>
    <b>Cell:</b> 340-555-0147<br>
    <b>Email:</b> dholloway@mailvessel.com<br>
    <b>License No.:</b> 472916
  </div>
</section>

<section class="sheet card-green" aria-label="Business card back, green">
  <div class="mark"><span class="mark-circle"></span><span class="mark-name">Brisk Meadow</span></div>
</section>

<section class="sheet card-blue" aria-label="Business card back, blue">
  <div class="mark"><span class="mark-circle"></span><span class="mark-name">Brisk Meadow</span></div>
</section>

<section class="sheet card-gray" aria-label="Business card back, silver">
  <div class="mark"><span class="mark-circle"></span><span class="mark-name">Brisk Meadow</span></div>
</section>

<section class="sheet envelope" aria-label="Envelope">
  <svg class="deco" viewBox="0 0 581 295" preserveAspectRatio="none">
    <path d="M0 0 H581 V30 H320 Q290 62 260 30 H0 Z" fill="var(--blue)"/>
    <path d="M0 0 H581 V18 H315 Q290 48 265 18 H0 Z" fill="var(--blue-deep)"/>
    <path d="M470 295 Q540 170 500 30 L581 30 L581 295 Z" fill="var(--gray)"/>
    <path d="M490 295 Q556 170 520 30 L581 30 L581 295 Z" fill="var(--blue)"/>
    <path d="M520 295 Q570 170 548 30 L581 30 L581 295 Z" fill="var(--blue-deep)"/>
  </svg>
  <span class="flap-circle"></span>
  <div class="brand"><span class="brand-dot"></span><span class="brand-name">Brisk Meadow</span></div>
  <div class="env-address">P.O. Box 618207<br>Christiansted, St. Croix 00822</div>
</section>

<section class="sheet letterhead" aria-label="Letterhead">
  <svg class="deco" viewBox="0 0 523 701" preserveAspectRatio="none">
    <path d="M330 0 Q520 350 330 701 L523 701 L523 0 Z" fill="var(--gray)"/>
    <path d="M380 0 Q540 350 380 701 L523 701 L523 0 Z" fill="var(--blue)"/>
    <path d="M450 0 Q560 350 450 701 L523 701 L523 0 Z" fill="var(--blue-deep)"/>
  </svg>
  <div class="brand"><span class="brand-dot"></span><span class="brand-name">Brisk Meadow</span></div>
  <div class="lh-footer">
    P.O. Box 618207, Christiansted, St. Croix 00822<br>
    <b>Phone:</b> 340-555-0182 &nbsp;|&nbsp; <b>Cell:</b> 340-555-0147<br>
    <b>Email:</b> Briskmeadowcoolingandyardcraft@mailvessel.com<br>
    <b>License No.:</b> 472916
  </div>
</section>

</body>
</html>
```